4K Business Card Design

We need a business card that emphasizes consulting services worldwide. The name of the company is KKKK Consulting Group. We provide consulting services across several industries including but not limited to commodities, telecom, manufacturing, logistics, marketing and operations. We would like to see a creative design that emphasizes the global aspect, including Latin America and US markets, as well the bilingual nature of the service offerings.

The contact information section should include icons to represent the following data:
1) Name, Title and Company Name
2) Mobile Number
3) ChatLine ID
4) Email
5) Web Page
6) Location

We would like to see a card that emphasizes the worldwide concept. The back of the card should be simple, including only the logo (or a portion of the logo) and the slogan.

We would also like to see business cards in a booklet format. The colors to be used should be the same combination of colors used in the logos attached to this brief.

The logo design and some business card examples from Artful Herd are attached for reference on style and look.

Target Market(s)

International business executives, 45-65 years of age, bilingual

Industry/Entity Type

Marketing

Colors
0792cd
34a7d8
85cae6
ffffff
cee9f5
ecf7fb

Requirements
Must have
• Please follow colors in logo attached.

2) Mobile Number
3) ChatLine ID
4) Email
5) Web Page
6) Location
Nice to have
• Global concept, consulting profile, diverse industry focus
Should not have
• No black color

```html
<!DOCTYPE html>
<html lang="en">
<head>
<meta charset="utf-8">
<title>KKKK Consulting Group – Business Card</title>
<link rel="stylesheet" href="https://fonts.googleapis.com/css2?family=Tinos:wght@400;700&display=swap">
<style>
  :root {
    --stage: #4b4e56;
    --blue-deep: #0792cd;
    --blue-mid: #34a7d8;
    --blue-soft: #85cae6;
    --blue-pale: #cee9f5;
    --blue-mist: #ecf7fb;
    --white: #ffffff;
    --ink-blue: #7fb0d8;
    --serif: "Tinos", "Times New Roman", serif;
  }
  * { box-sizing: border-box; margin: 0; padding: 0; }
  html, body { width: 1200px; height: 1000px; overflow: hidden; background: var(--stage); }
  .canvas { position: relative; width: 1200px; height: 1000px; font-family: var(--serif); }

  .card { position: absolute; width: 820px; height: 466px; border-radius: 22px; overflow: hidden; }

  /* Front */
  .card-front {
    left: 22px; top: 22px;
    background: radial-gradient(ellipse 55% 65% at 50% 48%, var(--white) 0%, var(--blue-pale) 22%, var(--blue-mid) 62%, var(--blue-deep) 100%);
  }
  .panel {
    position: absolute; border-radius: 16px;
    border: 2px solid rgba(255,255,255,0.35);
    background: rgba(255,255,255,0.08);
    box-shadow: inset 0 2px 6px rgba(255,255,255,0.35), inset 0 -3px 6px rgba(0,60,110,0.25);
  }
  .panel-identity { left: 53px; top: 23px; width: 716px; height: 112px; }
  .panel-contact { left: 53px; top: 353px; width: 716px; height: 98px; }

  .person-name {
    position: absolute; left: 0; right: 0; top: 34px; text-align: center;
    font-size: 54px; line-height: 1; color: var(--blue-mist);
    text-shadow: 0 1px 2px rgba(0,60,110,0.35);
  }
  .person-role {
    position: absolute; left: 0; right: 0; top: 86px; text-align: center;
    font-size: 33px; line-height: 1; color: var(--white);
    text-shadow: 0 1px 2px rgba(0,60,110,0.35);
  }
  .globe {
    position: absolute; left: 294px; top: 128px; width: 234px; height: 234px; border-radius: 50%;
    background: radial-gradient(circle at 60% 60%, var(--blue-pale) 0%, var(--blue-soft) 45%, #2a5f86 85%, #1b3e5c 100%);
  }
  .contact { position: absolute; left: 0; right: 0; color: var(--white); font-size: 20px; line-height: 1; }
  .contact-row { position: absolute; left: 0; right: 0; text-align: center; }
  .contact-mobile { position: absolute; left: 163px; top: 361px; }
  .contact-chat { position: absolute; left: 484px; top: 361px; }
  .contact-web { top: 382px; }
  .contact-email { top: 402px; }
  .contact-address { top: 422px; }

  /* Back */
  .card-back {
    left: 347px; top: 508px;
    background: linear-gradient(180deg, var(--blue-soft) 0%, var(--blue-mist) 30%, var(--white) 55%, var(--blue-mist) 78%, var(--blue-soft) 100%);
  }
  .band {
    position: absolute; left: 60px; width: 701px; height: 72px; border-radius: 14px;
    background: linear-gradient(180deg, var(--blue-mist) 0%, var(--blue-pale) 55%, var(--blue-soft) 100%);
    box-shadow: 0 2px 3px rgba(40,110,170,0.35), inset 0 1px 2px var(--white);
  }
  .band-company { top: 25px; }
  .band-slogan { top: 370px; }
  .band-text {
    position: absolute; left: 0; right: 0; top: 10px; text-align: center;
    font-size: 54px; line-height: 1; color: var(--ink-blue);
    text-shadow: 0 1px 0 var(--white), 0 2px 2px rgba(30,80,130,0.45);
  }
  .brand {
    position: absolute; left: 0; right: 0; top: 195px;
    display: flex; align-items: center; justify-content: center; gap: 18px;
  }
  .brand-square { width: 44px; height: 44px; background: var(--ink-blue); }
  .brand-name { font-size: 80px; line-height: 1; color: var(--ink-blue); }
</style>
</head>
<body>
<main class="canvas">
  <section class="card card-front" aria-label="Business card front">
    <div class="panel panel-identity"></div>
    <p class="person-name">Alan Reyes</p>
    <p class="person-role">President &amp; CEO,KKKK Consulting Group</p>
    <div class="globe" role="img" aria-label="Glass globe illustration with glowing connection network"></div>
    <div class="panel panel-contact"></div>
    <div class="contact">
      <span class="contact-mobile">Mobile: 555 210 4477</span>
      <span class="contact-chat">ChatLine ID: AlanReyes</span>
    </div>
    <div class="contact">
      <p class="contact-row contact-web">Web: www.kkkkgroup.com</p>
      <p class="contact-row contact-email">Email: hello@kkkkgroup.com</p>
      <p class="contact-row contact-address">Address: 4820,Harbor RD,Suite 204,Lakeview,TX,75001</p>
    </div>
  </section>

  <section class="card card-back" aria-label="Business card back">
    <div class="band band-company"><p class="band-text">KKKK Consulting Group</p></div>
    <div class="brand">
      <span class="brand-square"></span>
      <span class="brand-name">4K</span>
    </div>
    <div class="band band-slogan"><p class="band-text">“Insert slogan here”</p></div>
  </section>
</main>
</body>
</html>
```